COMPANY SIGN

I am in the process of ordering new company For Sale signs and stationary (business cards, envelopes, letterheads, and labels). I need a new design with my existing company logo. The TWO MOST IMPORTANT PROJECTS I need right now is the new design for the company sign and business cards. I've uploaded a .jpg file of my company logo.

I like the design to be eye catching and the background color of the company sign to be soothing to the eyes. Perhaps, using one of the color on the leaves of the logo or any other color that the designer think will go well with the logo. My favorite colors are teal or light olive color but don't let that affect your creativity.

Industry/Entity Type

Business

Requirements
Should not have
• Please don't use "Times New Roman" fonts or fonts that is hard to read.

```html
<!DOCTYPE html>
<html lang="en">
<head>
<meta charset="utf-8">
<title>Parkside Home Walk – Square Card</title>
<link rel="stylesheet" href="https://fonts.googleapis.com/css2?family=Open+Sans:wght@400;600&display=swap">
<style>
  :root {
    --page-bg: #eceef0;
    --card-frame: #8fa556;
    --card-light: #fbfcf7;
    --card-mid: #c9d9a3;
    --card-deep: #a5c06a;
    --ink-brown: #4a3528;
    --url-navy: #2c4a8a;
    --url-orange: #d9541e;
    --url-grey: #7c7c7c;
  }
  * { margin: 0; padding: 0; box-sizing: border-box; }
  html, body {
    width: 800px;
    height: 1200px;
    overflow: hidden;
    background: var(--page-bg);
    font-family: "Open Sans", Arial, sans-serif;
  }
  .canvas {
    width: 800px;
    height: 1200px;
    display: flex;
    align-items: center;
    justify-content: center;
  }
  .square-card {
    width: 520px;
    height: 520px;
    border-radius: 34px;
    background: var(--card-frame);
    padding: 14px;
    box-shadow: 0 6px 18px rgba(0,0,0,0.12);
  }
  .card-face {
    width: 100%;
    height: 100%;
    border-radius: 24px;
    background:
      radial-gradient(ellipse 90% 55% at 25% 8%, var(--card-light) 0%, rgba(251,252,247,0) 70%),
      linear-gradient(165deg, var(--card-light) 0%, var(--card-mid) 45%, var(--card-deep) 100%);
    display: flex;
    flex-direction: column;
    align-items: center;
    padding-top: 120px;
  }
  .brand {
    display: flex;
    align-items: center;
    gap: 14px;
  }
  .brand-dot {
    width: 22px;
    height: 22px;
    border-radius: 50%;
    background: var(--ink-brown);
  }
  .brand-name {
    font-size: 40px;
    font-weight: 400;
    color: var(--ink-brown);
    letter-spacing: 0.5px;
  }
  .phone {
    margin-top: 96px;
    font-size: 42px;
    font-weight: 400;
    color: var(--ink-brown);
    letter-spacing: 1px;
  }
  .web {
    margin-top: 26px;
    font-size: 19px;
    color: var(--ink-brown);
  }
  .web .w-navy { color: var(--url-navy); }
  .web .w-orange { color: var(--url-orange); }
  .web .w-grey { color: var(--url-grey); }
</style>
</head>
<body>
  <main class="canvas">
    <section class="square-card">
      <div class="card-face">
        <div class="brand">
          <span class="brand-dot"></span>
          <span class="brand-name">Parkside Home Walk</span>
        </div>
        <p class="phone">555.014.2290</p>
        <p class="web">www.<span class="w-navy">Parkside</span><span class="w-orange">Home</span><span class="w-grey">Walk</span>.com</p>
      </div>
    </section>
  </main>
</body>
</html>
```